fizzy drinks label design

I want to design fizzy drink label for 3 flavors : black grapes, red apple and mojito, band name kestrola, product name KOLTA , product will be in plastic bottle, label size 198 mm X 66mm

```html
<!DOCTYPE html>
<html lang="en">
<head>
<meta charset="utf-8">
<title>kestrola KOLTA – fizzy drink labels</title>
<link href="https://fonts.googleapis.com/css2?family=Courier+Prime:wght@400;700&display=swap" rel="stylesheet">
<style>
  :root {
    --page: #ffffff;
    --label-black: #000000;
    --ink: #ffffff;
    --oval-deep: #1d3a6e;
    --oval-mid: #2a6a9a;
    --oval-light: #3b8fb5;
    --grape: #b070d0;
    --apple: #e0383a;
    --mint: #7fd66a;
  }
  html, body {
    margin: 0;
    width: 1200px;
    height: 813px;
    overflow: hidden;
    background: var(--page);
  }
  .sheet {
    width: 1200px;
    height: 813px;
    display: flex;
    flex-direction: column;
    align-items: center;
    justify-content: center;
    gap: 26px;
  }
  .label {
    display: block;
    width: 660px;
    height: 237px;
  }
  .label-bg { fill: var(--label-black); }
  .info-text, .ingredients-text, .volume, .nutrition-text, .nutrition-fine {
    font-family: "Courier Prime", "Courier New", monospace;
    fill: var(--ink);
  }
  .info-text { font-size: 13px; }
  .ingredients-text { font-size: 12px; }
  .nutrition-text { font-size: 10px; }
  .nutrition-fine { font-size: 7.5px; }
  .nutrition-rule { stroke: var(--ink); stroke-width: 1; fill: none; }
  .volume { font-size: 20px; }
  .brand-name {
    font-family: "Courier Prime", "Courier New", monospace;
    font-weight: 700;
    font-size: 38px;
    fill: var(--ink);
  }
  .brand-dot { fill: var(--ink); }
  .product-name {
    font-family: "Courier Prime", "Courier New", monospace;
    font-weight: 700;
    font-size: 112px;
    fill: var(--ink);
  }
  .flavour-name {
    font-family: "Courier Prime", "Courier New", monospace;
    font-size: 28px;
    fill: var(--ink);
  }
  .icon { fill: none; stroke: var(--ink); stroke-width: 2; }
  .icon-fill { fill: var(--ink); }
  .icon-caption {
    font-family: "Courier Prime", "Courier New", monospace;
    font-size: 7px;
    fill: var(--ink);
  }
</style>
</head>
<body>
<main class="sheet">

  <svg class="label" viewBox="0 0 1150 413" aria-label="kestrola KOLTA black grapes label">
    <defs>
      <radialGradient id="oval-fill" cx="0.55" cy="0.35" r="0.7">
        <stop offset="0" stop-color="var(--oval-light)"/>
        <stop offset="0.6" stop-color="var(--oval-mid)"/>
        <stop offset="1" stop-color="var(--oval-deep)"/>
      </radialGradient>
      <mask id="oval-bite">
        <rect width="1150" height="413" fill="#fff"/>
        <circle cx="315" cy="265" r="85" fill="#000"/>
      </mask>
      <radialGradient id="fizz-grape">
        <stop offset="0" stop-color="var(--grape)" stop-opacity="0.85"/>
        <stop offset="0.7" stop-color="var(--grape)" stop-opacity="0.45"/>
        <stop offset="1" stop-color="var(--grape)" stop-opacity="0"/>
      </radialGradient>
    </defs>
    <rect class="label-bg" width="1150" height="413"/>

    <g class="producer-info">
      <text class="info-text" x="100" y="40">Produced by:</text>
      <text class="info-text" x="100" y="56">kestrola</text>
      <text class="info-text" x="100" y="72">123 Name st.</text>
      <text class="info-text" x="100" y="88">City 12345</text>
      <text class="info-text" x="100" y="104">Country</text>
      <text class="info-text" x="100" y="135">Lot: NM123456</text>
      <text class="info-text" x="100" y="166">Best before:</text>
      <text class="info-text" x="100" y="182">01/02/2023</text>
      <text class="info-text" x="100" y="213">Keep cool.</text>
      <text class="info-text" x="100" y="229">Serve cool.</text>
      <g class="care-icons">
        <path class="icon" d="M102 255 h14 l-3 14 h-8 z M109 269 v6 M104 277 h10 M120 255 v22 M123 255 v8 h-6"/>
        <path class="icon" d="M151 258 l9 -6 l9 6 M146 274 l6 -10 M174 274 l-6 -10 M148 276 h24"/>
        <text class="icon-caption" x="151" y="288">PET</text>
        <circle class="icon" cx="191" cy="266" r="9"/>
        <path class="icon-fill" d="M188 258 l6 0 l-3 5 z M199 271 l-3 5 l-3 -5 z M182 270 l3 -5 l3 5 z"/>
        <path class="icon" d="M221 262 h12 l-2 16 h-8 z M219 262 h16"/>
        <circle class="icon-fill" cx="235" cy="253" r="2.5"/>
      </g>
    </g>

    <g class="brand-badge">
      <path mask="url(#oval-bite)" fill="url(#oval-fill)" d="M400 110 C440 50 560 20 660 35 C760 50 800 140 785 230 C770 320 680 385 560 382 C450 380 380 320 372 240 C368 190 375 150 400 110 Z"/>
      <ellipse role="img" aria-label="glowing purple fizz bubbles rising across the badge" cx="600" cy="200" rx="200" ry="95" transform="rotate(-22 600 200)" fill="url(#fizz-grape)"/>
      <g transform="translate(560 82) rotate(-14)">
        <circle class="brand-dot" cx="-108" cy="-11" r="7"/>
        <text class="brand-name" x="0" y="0" text-anchor="middle">kestrola</text>
      </g>
      <text class="product-name" text-anchor="middle" transform="translate(632 262) rotate(-24)">KOLTA</text>
      <text class="flavour-name" text-anchor="middle" transform="translate(655 345) rotate(-20)">black grapes</text>
    </g>

    <text class="volume" x="777" y="378">123 ml</text>

    <g class="ingredients">
      <text class="ingredients-text" x="934" y="40" textLength="160" lengthAdjust="spacingAndGlyphs">INGREDIENTS: lorem, ipsum,</text>
      <text class="ingredients-text" x="934" y="56" textLength="152" lengthAdjust="spacingAndGlyphs">dolor, sit, amet, consectetur,</text>
      <text class="ingredients-text" x="934" y="72" textLength="156" lengthAdjust="spacingAndGlyphs">adipiscing, elit, duis, portitor,</text>
      <text class="ingredients-text" x="934" y="88" textLength="152" lengthAdjust="spacingAndGlyphs">fusce vestibulum, orci, nunc,</text>
      <text class="ingredients-text" x="934" y="104" textLength="152" lengthAdjust="spacingAndGlyphs">auctor, ultricies, fermentum,</text>
      <text class="ingredients-text" x="934" y="120" textLength="160" lengthAdjust="spacingAndGlyphs">vitae, ligula, convallis, laoreet,</text>
      <text class="ingredients-text" x="934" y="136" textLength="126" lengthAdjust="spacingAndGlyphs">placerat, praesent, eget,</text>
      <text class="ingredients-text" x="934" y="152" textLength="144" lengthAdjust="spacingAndGlyphs">ultrices, mauris, vulputate,</text>
      <text class="ingredients-text" x="934" y="168" textLength="100" lengthAdjust="spacingAndGlyphs">diam, quisque, nisi.</text>
    </g>

    <g class="nutrition-facts">
      <rect class="nutrition-rule" x="934" y="176" width="174" height="206"/>
      <text class="nutrition-text" x="937" y="186" textLength="86" lengthAdjust="spacingAndGlyphs">NUTRITION FACTS</text>
      <text class="nutrition-text" x="937" y="198" textLength="140" lengthAdjust="spacingAndGlyphs">Serving size: 1 bottle (345 ml)</text>
      <text class="nutrition-text" x="937" y="210" textLength="117" lengthAdjust="spacingAndGlyphs">Servings per container: 1</text>
      <line class="nutrition-rule" x1="937" y1="219" x2="1105" y2="219"/>
      <text class="nutrition-text" x="937" y="233" textLength="94" lengthAdjust="spacingAndGlyphs">Amount per serving:</text>
      <text class="nutrition-text" x="937" y="244">calories <tspan font-weight="700">123</tspan></text>
      <line class="nutrition-rule" x1="937" y1="252" x2="1105" y2="252"/>
      <text class="nutrition-text" x="1104" y="268" text-anchor="end">% daily value*</text>
      <text class="nutrition-text" x="937" y="280">Total fat 0 g</text><text class="nutrition-text" x="1104" y="280" text-anchor="end">0%</text>
      <text class="nutrition-text" x="937" y="292">Sodium 12 g</text><text class="nutrition-text" x="1104" y="292" text-anchor="end">1%</text>
      <text class="nutrition-text" x="937" y="304">Total carb 34 g</text><text class="nutrition-text" x="1104" y="304" text-anchor="end">10%</text>
      <text class="nutrition-text" x="948" y="316">sugar 5 g</text>
      <text class="nutrition-text" x="937" y="328">Protein 0 g</text><text class="nutrition-text" x="1104" y="328" text-anchor="end">0%</text>
      <line class="nutrition-rule" x1="937" y1="337" x2="1105" y2="337"/>
      <text class="nutrition-fine" x="937" y="351" textLength="166" lengthAdjust="spacingAndGlyphs">* Percent Daily Values are based on a 2,000</text>
      <text class="nutrition-fine" x="937" y="363" textLength="162" lengthAdjust="spacingAndGlyphs">calorie diet. Your daily value may be higher</text>
      <text class="nutrition-fine" x="937" y="375" textLength="158" lengthAdjust="spacingAndGlyphs">or lower depending on your calorie needs.</text>
    </g>
  </svg>

  <svg class="label" viewBox="0 0 1150 413" aria-label="kestrola KOLTA red apple label">
    <defs>
      <radialGradient id="fizz-apple">
        <stop offset="0" stop-color="var(--apple)" stop-opacity="0.9"/>
        <stop offset="0.7" stop-color="var(--apple)" stop-opacity="0.5"/>
        <stop offset="1" stop-color="var(--apple)" stop-opacity="0"/>
      </radialGradient>
    </defs>
    <rect class="label-bg" width="1150" height="413"/>

    <g class="producer-info">
      <text class="info-text" x="100" y="40">Produced by:</text>
      <text class="info-text" x="100" y="56">kestrola</text>
      <text class="info-text" x="100" y="72">123 Name st.</text>
      <text class="info-text" x="100" y="88">City 12345</text>
      <text class="info-text" x="100" y="104">Country</text>
      <text class="info-text" x="100" y="135">Lot: NM123456</text>
      <text class="info-text" x="100" y="166">Best before:</text>
      <text class="info-text" x="100" y="182">01/02/2023</text>
      <text class="info-text" x="100" y="213">Keep cool.</text>
      <text class="info-text" x="100" y="229">Serve cool.</text>
      <g class="care-icons">
        <path class="icon" d="M102 255 h14 l-3 14 h-8 z M109 269 v6 M104 277 h10 M120 255 v22 M123 255 v8 h-6"/>
        <path class="icon" d="M151 258 l9 -6 l9 6 M146 274 l6 -10 M174 274 l-6 -10 M148 276 h24"/>
        <text class="icon-caption" x="151" y="288">PET</text>
        <circle class="icon" cx="191" cy="266" r="9"/>
        <path class="icon-fill" d="M188 258 l6 0 l-3 5 z M199 271 l-3 5 l-3 -5 z M182 270 l3 -5 l3 5 z"/>
        <path class="icon" d="M221 262 h12 l-2 16 h-8 z M219 262 h16"/>
        <circle class="icon-fill" cx="235" cy="253" r="2.5"/>
      </g>
    </g>

    <g class="brand-badge">
      <path mask="url(#oval-bite)" fill="url(#oval-fill)" d="M400 110 C440 50 560 20 660 35 C760 50 800 140 785 230 C770 320 680 385 560 382 C450 380 380 320 372 240 C368 190 375 150 400 110 Z"/>
      <ellipse role="img" aria-label="glowing red fizz bubbles rising across the badge" cx="600" cy="200" rx="200" ry="95" transform="rotate(-22 600 200)" fill="url(#fizz-apple)"/>
      <g transform="translate(560 82) rotate(-14)">
        <circle class="brand-dot" cx="-108" cy="-11" r="7"/>
        <text class="brand-name" x="0" y="0" text-anchor="middle">kestrola</text>
      </g>
      <text class="product-name" text-anchor="middle" transform="translate(632 262) rotate(-24)">KOLTA</text>
      <text class="flavour-name" text-anchor="middle" transform="translate(660 345) rotate(-20)">red apple</text>
    </g>

    <text class="volume" x="777" y="378">123 ml</text>

    <g class="ingredients">
      <text class="ingredients-text" x="934" y="40" textLength="160" lengthAdjust="spacingAndGlyphs">INGREDIENTS: lorem, ipsum,</text>
      <text class="ingredients-text" x="934" y="56" textLength="152" lengthAdjust="spacingAndGlyphs">dolor, sit, amet, consectetur,</text>
      <text class="ingredients-text" x="934" y="72" textLength="156" lengthAdjust="spacingAndGlyphs">adipiscing, elit, duis, portitor,</text>
      <text class="ingredients-text" x="934" y="88" textLength="152" lengthAdjust="spacingAndGlyphs">fusce vestibulum, orci, nunc,</text>
      <text class="ingredients-text" x="934" y="104" textLength="152" lengthAdjust="spacingAndGlyphs">auctor, ultricies, fermentum,</text>
      <text class="ingredients-text" x="934" y="120" textLength="160" lengthAdjust="spacingAndGlyphs">vitae, ligula, convallis, laoreet,</text>
      <text class="ingredients-text" x="934" y="136" textLength="126" lengthAdjust="spacingAndGlyphs">placerat, praesent, eget,</text>
      <text class="ingredients-text" x="934" y="152" textLength="144" lengthAdjust="spacingAndGlyphs">ultrices, mauris, vulputate,</text>
      <text class="ingredients-text" x="934" y="168" textLength="100" lengthAdjust="spacingAndGlyphs">diam, quisque, nisi.</text>
    </g>

    <g class="nutrition-facts">
      <rect class="nutrition-rule" x="934" y="176" width="174" height="206"/>
      <text class="nutrition-text" x="937" y="186" textLength="86" lengthAdjust="spacingAndGlyphs">NUTRITION FACTS</text>
      <text class="nutrition-text" x="937" y="198" textLength="140" lengthAdjust="spacingAndGlyphs">Serving size: 1 bottle (345 ml)</text>
      <text class="nutrition-text" x="937" y="210" textLength="117" lengthAdjust="spacingAndGlyphs">Servings per container: 1</text>
      <line class="nutrition-rule" x1="937" y1="219" x2="1105" y2="219"/>
      <text class="nutrition-text" x="937" y="233" textLength="94" lengthAdjust="spacingAndGlyphs">Amount per serving:</text>
      <text class="nutrition-text" x="937" y="244">calories <tspan font-weight="700">123</tspan></text>
      <line class="nutrition-rule" x1="937" y1="252" x2="1105" y2="252"/>
      <text class="nutrition-text" x="1104" y="268" text-anchor="end">% daily value*</text>
      <text class="nutrition-text" x="937" y="280">Total fat 0 g</text><text class="nutrition-text" x="1104" y="280" text-anchor="end">0%</text>
      <text class="nutrition-text" x="937" y="292">Sodium 12 g</text><text class="nutrition-text" x="1104" y="292" text-anchor="end">1%</text>
      <text class="nutrition-text" x="937" y="304">Total carb 34 g</text><text class="nutrition-text" x="1104" y="304" text-anchor="end">10%</text>
      <text class="nutrition-text" x="948" y="316">sugar 5 g</text>
      <text class="nutrition-text" x="937" y="328">Protein 0 g</text><text class="nutrition-text" x="1104" y="328" text-anchor="end">0%</text>
      <line class="nutrition-rule" x1="937" y1="337" x2="1105" y2="337"/>
      <text class="nutrition-fine" x="937" y="351" textLength="166" lengthAdjust="spacingAndGlyphs">* Percent Daily Values are based on a 2,000</text>
      <text class="nutrition-fine" x="937" y="363" textLength="162" lengthAdjust="spacingAndGlyphs">calorie diet. Your daily value may be higher</text>
      <text class="nutrition-fine" x="937" y="375" textLength="158" lengthAdjust="spacingAndGlyphs">or lower depending on your calorie needs.</text>
    </g>
  </svg>

  <svg class="label" viewBox="0 0 1150 413" aria-label="kestrola KOLTA mojito label">
    <defs>
      <radialGradient id="fizz-mint">
        <stop offset="0" stop-color="var(--mint)" stop-opacity="0.85"/>
        <stop offset="0.7" stop-color="var(--mint)" stop-opacity="0.45"/>
        <stop offset="1" stop-color="var(--mint)" stop-opacity="0"/>
      </radialGradient>
    </defs>
    <rect class="label-bg" width="1150" height="413"/>

    <g class="producer-info">
      <text class="info-text" x="100" y="40">Produced by:</text>
      <text class="info-text" x="100" y="56">kestrola</text>
      <text class="info-text" x="100" y="72">123 Name st.</text>
      <text class="info-text" x="100" y="88">City 12345</text>
      <text class="info-text" x="100" y="104">Country</text>
      <text class="info-text" x="100" y="135">Lot: NM123456</text>
      <text class="info-text" x="100" y="166">Best before:</text>
      <text class="info-text" x="100" y="182">01/02/2023</text>
      <text class="info-text" x="100" y="213">Keep cool.</text>
      <text class="info-text" x="100" y="229">Serve cool.</text>
      <g class="care-icons">
        <path class="icon" d="M102 255 h14 l-3 14 h-8 z M109 269 v6 M104 277 h10 M120 255 v22 M123 255 v8 h-6"/>
        <path class="icon" d="M151 258 l9 -6 l9 6 M146 274 l6 -10 M174 274 l-6 -10 M148 276 h24"/>
        <text class="icon-caption" x="151" y="288">PET</text>
        <circle class="icon" cx="191" cy="266" r="9"/>
        <path class="icon-fill" d="M188 258 l6 0 l-3 5 z M199 271 l-3 5 l-3 -5 z M182 270 l3 -5 l3 5 z"/>
        <path class="icon" d="M221 262 h12 l-2 16 h-8 z M219 262 h16"/>
        <circle class="icon-fill" cx="235" cy="253" r="2.5"/>
      </g>
    </g>

    <g class="brand-badge">
      <path mask="url(#oval-bite)" fill="url(#oval-fill)" d="M400 110 C440 50 560 20 660 35 C760 50 800 140 785 230 C770 320 680 385 560 382 C450 380 380 320 372 240 C368 190 375 150 400 110 Z"/>
      <ellipse role="img" aria-label="glowing green fizz bubbles rising across the badge" cx="600" cy="200" rx="200" ry="95" transform="rotate(-22 600 200)" fill="url(#fizz-mint)"/>
      <g transform="translate(560 82) rotate(-14)">
        <circle class="brand-dot" cx="-108" cy="-11" r="7"/>
        <text class="brand-name" x="0" y="0" text-anchor="middle">kestrola</text>
      </g>
      <text class="product-name" text-anchor="middle" transform="translate(632 262) rotate(-24)">KOLTA</text>
      <text class="flavour-name" text-anchor="middle" transform="translate(660 350) rotate(-20)">mojito</text>
    </g>

    <text class="volume" x="777" y="378">123 ml</text>

    <g class="ingredients">
      <text class="ingredients-text" x="934" y="40" textLength="160" lengthAdjust="spacingAndGlyphs">INGREDIENTS: lorem, ipsum,</text>
      <text class="ingredients-text" x="934" y="56" textLength="152" lengthAdjust="spacingAndGlyphs">dolor, sit, amet, consectetur,</text>
      <text class="ingredients-text" x="934" y="72" textLength="156" lengthAdjust="spacingAndGlyphs">adipiscing, elit, duis, portitor,</text>
      <text class="ingredients-text" x="934" y="88" textLength="152" lengthAdjust="spacingAndGlyphs">fusce vestibulum, orci, nunc,</text>
      <text class="ingredients-text" x="934" y="104" textLength="152" lengthAdjust="spacingAndGlyphs">auctor, ultricies, fermentum,</text>
      <text class="ingredients-text" x="934" y="120" textLength="160" lengthAdjust="spacingAndGlyphs">vitae, ligula, convallis, laoreet,</text>
      <text class="ingredients-text" x="934" y="136" textLength="126" lengthAdjust="spacingAndGlyphs">placerat, praesent, eget,</text>
      <text class="ingredients-text" x="934" y="152" textLength="144" lengthAdjust="spacingAndGlyphs">ultrices, mauris, vulputate,</text>
      <text class="ingredients-text" x="934" y="168" textLength="100" lengthAdjust="spacingAndGlyphs">diam, quisque, nisi.</text>
    </g>

    <g class="nutrition-facts">
      <rect class="nutrition-rule" x="934" y="176" width="174" height="206"/>
      <text class="nutrition-text" x="937" y="186" textLength="86" lengthAdjust="spacingAndGlyphs">NUTRITION FACTS</text>
      <text class="nutrition-text" x="937" y="198" textLength="140" lengthAdjust="spacingAndGlyphs">Serving size: 1 bottle (345 ml)</text>
      <text class="nutrition-text" x="937" y="210" textLength="117" lengthAdjust="spacingAndGlyphs">Servings per container: 1</text>
      <line class="nutrition-rule" x1="937" y1="219" x2="1105" y2="219"/>
      <text class="nutrition-text" x="937" y="233" textLength="94" lengthAdjust="spacingAndGlyphs">Amount per serving:</text>
      <text class="nutrition-text" x="937" y="244">calories <tspan font-weight="700">123</tspan></text>
      <line class="nutrition-rule" x1="937" y1="252" x2="1105" y2="252"/>
      <text class="nutrition-text" x="1104" y="268" text-anchor="end">% daily value*</text>
      <text class="nutrition-text" x="937" y="280">Total fat 0 g</text><text class="nutrition-text" x="1104" y="280" text-anchor="end">0%</text>
      <text class="nutrition-text" x="937" y="292">Sodium 12 g</text><text class="nutrition-text" x="1104" y="292" text-anchor="end">1%</text>
      <text class="nutrition-text" x="937" y="304">Total carb 34 g</text><text class="nutrition-text" x="1104" y="304" text-anchor="end">10%</text>
      <text class="nutrition-text" x="948" y="316">sugar 5 g</text>
      <text class="nutrition-text" x="937" y="328">Protein 0 g</text><text class="nutrition-text" x="1104" y="328" text-anchor="end">0%</text>
      <line class="nutrition-rule" x1="937" y1="337" x2="1105" y2="337"/>
      <text class="nutrition-fine" x="937" y="351" textLength="166" lengthAdjust="spacingAndGlyphs">* Percent Daily Values are based on a 2,000</text>
      <text class="nutrition-fine" x="937" y="363" textLength="162" lengthAdjust="spacingAndGlyphs">calorie diet. Your daily value may be higher</text>
      <text class="nutrition-fine" x="937" y="375" textLength="158" lengthAdjust="spacingAndGlyphs">or lower depending on your calorie needs.</text>
    </g>
  </svg>

</main>
</body>
</html>
```